Tolvek Pens is looking for a new packaging for their BallPen Quillon

We need a brand new packaging design for our product Quillon. We at Tolvek pens manufacture high quality ball pens and need a packaging design which justifies the brand and the product. We are looking for a 5pcs pouch and a 10pcs pouch design for the same product. The product will be launched in the 2 packagings simultaneously. The two packagings need to be themed to look similar to each other. Only difference being the size. The attached pictures and images will make it easier to understand

Target Market(s)

Retail sales- Wholesalers and distributors in India

Industry/Entity Type

Manufacture

Requirements
Must have
• attractive colours
• visibility of product
Nice to have
• yellow and orange colours
Should not have
• avoid red, blue and black colours
• too much abstract designing
• cluttered designs
• attached images of pouches from the competitors are only for reference. We don't like any of those designs

```html
<!DOCTYPE html>
<html lang="en">
<head>
<meta charset="utf-8">
<title>Tolvek Quillon Ball Pen – 5 pcs pouch</title>
<link rel="stylesheet" href="https://fonts.googleapis.com/css2?family=Michroma&display=swap">
<style>
  :root{
    --stage:#e4e4e4;
    --header-yellow:#f2e51c;
    --header-shade:#e0d20e;
    --ink:#151515;
    --pouch-film:#d9dadd;
    --pouch-film-light:#eeeff1;
    --pouch-edge:#bfc1c5;
    --band-dark:#111111;
    --pen-violet:#54279a;
    --pen-violet-light:#8d6cc4;
    --tag-black:#1b1b1b;
    --tag-yellow:#f3e21a;
    --card-white:#f7f7f7;
    --white:#ffffff;
    --badge:#2b2b2b;
  }
  *{box-sizing:border-box;margin:0;padding:0}
  html,body{width:1200px;height:1200px;overflow:hidden}
  body{background:var(--stage);font-family:"Michroma",sans-serif;color:var(--ink)}
  .canvas{position:relative;width:1200px;height:1200px}

  .pouch{position:absolute;top:154px;height:908px}
  .pouch--front{left:110px;width:452px}
  .pouch--back{left:620px;width:472px}

  .pouch__film{position:absolute;inset:98px 0 0 0;
    background:linear-gradient(90deg,var(--pouch-film) 0%,var(--pouch-film-light) 18%,var(--pouch-film-light) 82%,var(--pouch-film) 100%);
    border:1px solid var(--pouch-edge);border-top:none;overflow:hidden}

  .pouch__header{position:absolute;left:0;top:0;width:100%;height:98px;
    background:linear-gradient(180deg,var(--header-yellow) 0%,var(--header-yellow) 85%,var(--header-shade) 100%);
    display:flex;align-items:center;justify-content:center}
  .hang-slot{position:absolute;top:14px;left:50%;width:38px;height:14px;margin-left:-19px;
    border-radius:7px;background:var(--stage);box-shadow:inset 0 1px 2px rgba(0,0,0,.25)}
  .brand-name{font-size:30px;letter-spacing:4px;color:var(--ink);margin-top:22px;text-transform:uppercase}

  /* front */
  .pens-visual{position:absolute;left:38px;top:90px;width:376px;height:720px;
    background:linear-gradient(90deg,rgba(84,39,154,.15),rgba(84,39,154,.55) 50%,rgba(84,39,154,.15))}
  .name-band{position:absolute;left:0;top:0;width:100%;height:142px;
    background:linear-gradient(180deg,var(--band-dark) 0%,rgba(17,17,17,.85) 70%,rgba(17,17,17,0) 100%);
    padding:34px 0 0 58px;color:var(--white)}
  .name-band__title{font-size:19px;letter-spacing:1px;text-transform:uppercase}
  .name-band__price{font-size:8px;line-height:11px;margin:10px 0 0 128px;text-transform:uppercase}
  .ornament{position:absolute}
  .ornament--front{left:0;bottom:0;width:100%;height:440px}
  .ornament--back{right:0;bottom:0;width:300px;height:320px}

  .feature-tags{position:absolute;left:190px;top:492px;list-style:none}
  .feature-tag{height:34px;margin-bottom:14px;background:var(--tag-black);color:var(--tag-yellow);
    font-size:14px;line-height:34px;text-transform:uppercase;padding-left:12px;width:250px;border:1px solid #555;white-space:nowrap}
  .feature-tag:nth-child(2){margin-left:10px;width:240px}
  .feature-tag:last-child{margin-left:28px;width:222px}

  .count-badge{position:absolute;border-radius:50%;background:var(--badge);color:var(--white);
    display:flex;flex-direction:column;align-items:center;justify-content:center;line-height:1}
  .count-badge--front{left:341px;top:674px;width:76px;height:76px}
  .count-badge--front .count-badge__num{font-size:30px}
  .count-badge__unit{font-size:10px;margin-top:3px}

  /* back */
  .header-count{position:absolute;right:20px;top:34px;width:52px;height:52px;border-radius:50%;
    background:var(--badge);color:var(--header-yellow);font-size:24px;display:flex;align-items:center;justify-content:center}
  .header-url{position:absolute;left:0;width:100%;bottom:4px;text-align:center;font-size:7px;color:var(--ink)}
  .info-card{position:absolute;left:30px;top:60px;width:412px;height:650px;background:var(--card-white)}
  .count-badge--back{left:-32px;top:78px;width:120px;height:120px}
  .count-badge--back .count-badge__num{font-size:56px}
  .count-badge--back .count-badge__unit{font-size:14px}
  .product-lines{position:absolute;left:128px;top:84px;font-size:13px;line-height:20px;text-transform:uppercase}
  .product-lines__price{font-size:9px;line-height:13px;margin-top:8px}
  .pen-visual{position:absolute;left:48px;top:300px;width:320px;height:36px;transform:rotate(-22deg);
    background:linear-gradient(90deg,var(--pen-violet-light),var(--pen-violet));border-radius:6px}
  .maker{position:absolute;left:15px;top:470px;font-size:9px;line-height:13px;text-transform:uppercase;width:200px}
  .maker__head{font-size:11px;margin-bottom:4px}
  .liability{position:absolute;left:225px;top:474px;font-size:8px;line-height:12px;text-transform:uppercase;width:175px}
  .contact{position:absolute;left:15px;top:570px;font-size:8px;line-height:13px;text-transform:uppercase}
  .contact__phone{font-size:11px}
  .packed{position:absolute;left:15px;top:630px;font-size:8px;text-transform:uppercase}
  .label-box{position:absolute;left:50px;top:712px;width:207px;height:80px;background:var(--white)}
  .footer-brand{position:absolute;right:22px;bottom:28px;font-size:14px;letter-spacing:2px;color:var(--white);text-transform:uppercase}
</style>
</head>
<body>
<main class="canvas">

  <section class="pouch pouch--front" aria-label="Front of 5 piece pouch">
    <div class="pouch__film">
      <div class="pens-visual" role="img" aria-label="Five violet Quillon ball pens inside the clear pouch"></div>
      <div class="name-band">
        <p class="name-band__title">Quillon ball pen</p>
        <p class="name-band__price">MRP Rs 5 per piece<br>MRP Rs 25 per pack</p>
      </div>
      <svg class="ornament ornament--front" role="img" aria-label="Olive and gold swirling decorative pattern" viewBox="0 0 452 440" preserveAspectRatio="none">
        <defs>
          <linearGradient id="ornFront" x1="0" y1="0" x2="1" y2="1">
            <stop offset="0" stop-color="#b59c35"/>
            <stop offset="1" stop-color="#5e4f18"/>
          </linearGradient>
        </defs>
        <path d="M0 40 C66 0 155 10 200 70 C244 140 222 220 288 270 C355 320 420 300 452 330 L452 440 L0 440 Z" fill="url(#ornFront)"/>
      </svg>
    </div>
    <header class="pouch__header">
      <span class="hang-slot"></span>
      <span class="brand-name">Tolvek</span>
    </header>
    <ul class="feature-tags">
      <li class="feature-tag">High quality tips</li>
      <li class="feature-tag">Long lasting ink</li>
      <li class="feature-tag">Super smooth</li>
    </ul>
    <div class="count-badge count-badge--front"><span class="count-badge__num">5</span><span class="count-badge__unit">PCS</span></div>
  </section>

  <section class="pouch pouch--back" aria-label="Back of 5 piece pouch">
    <div class="pouch__film">
      <svg class="ornament ornament--back" role="img" aria-label="Olive and gold swirling decorative pattern" viewBox="0 0 300 320" preserveAspectRatio="none">
        <defs>
          <linearGradient id="ornBack" x1="0" y1="0" x2="1" y2="1">
            <stop offset="0" stop-color="#b59c35"/>
            <stop offset="1" stop-color="#5e4f18"/>
          </linearGradient>
        </defs>
        <path d="M300 0 C240 30 200 40 150 90 C100 140 60 170 0 190 L0 320 L300 320 Z" fill="url(#ornBack)"/>
      </svg>
      <div class="info-card">
        <div class="count-badge count-badge--back"><span class="count-badge__num">5</span><span class="count-badge__unit">PCS</span></div>
        <div class="product-lines">
          <p>Tolvek<br>Quillon<br>Ball pen</p>
          <p class="product-lines__price">MRP Rs 5 per piece<br>MRP Rs 25 per pack</p>
        </div>
        <div class="pen-visual" role="img" aria-label="Illustration of a violet Quillon ball pen with its cap"></div>
        <div class="maker">
          <p class="maker__head">Manufactured by</p>
          <p>Tolvek Writing Instruments<br>An ISO 9001-2008 company<br>4418/4419,<br>2nd Phase Veldra,<br>Gujarat, India</p>
        </div>
        <p class="liability">Liability restricted to replacement of pen only</p>
        <div class="contact">
          <p>For feedback and queries</p>
          <p class="contact__phone">+ 123 555 010 010</p>
          <p>www.tolvek-pens.com</p>
        </div>
        <p class="packed">Packed date: 01/01/2020</p>
      </div>
      <div class="label-box"></div>
      <span class="footer-brand">Tolvek</span>
    </div>
    <header class="pouch__header">
      <span class="hang-slot"></span>
      <span class="brand-name">Tolvek</span>
      <span class="header-count">5</span>
      <span class="header-url">www.tolvek-pens.com</span>
    </header>
  </section>

</main>
</body>
</html>
```